Business cards for KORU Real Estate Holdings LLC

We need a cool, original business card design for a company based in the Washington DC metropolitan area. We are a new energetic and passionate Real Estate Investing Company that invests in all types of real estate; commercial, residential, industrial etc.

Our company color is Red since it reflects action, energy and speed; it is assertive confident, energizing, exciting, powerful, passionate and determined. So we would like business card communicate those qualities to the audience.

Our audiences are investors that want to invest with us, real estate sellers, buyers, and tenants who lease from us.

Our logo is attached

```html
<!DOCTYPE html>
<html lang="en">
<head>
<meta charset="utf-8">
<title>KORU Real Estate Holdings LLC – Business Cards</title>
<link rel="stylesheet" href="https://fonts.googleapis.com/css2?family=Open+Sans:wght@400;600;700;800&display=swap">
<style>
  :root {
    --stage: #2b2929;
    --card-dark: #1d1d1f;
    --panel-dark: #2a2a2c;
    --brand-red: #e0161f;
    --deep-red: #b80f17;
    --paper: #ffffff;
    --ink: #1f1f1f;
    --muted: #8d8d8d;
  }
  * { box-sizing: border-box; margin: 0; padding: 0; }
  html, body {
    width: 1200px; height: 716px; overflow: hidden;
    background: var(--stage);
    font-family: "Open Sans", Arial, sans-serif;
  }
  .stage { position: relative; width: 1200px; height: 716px; }

  .card {
    position: absolute; top: 208px;
    width: 525px; height: 300px;
    overflow: hidden;
    box-shadow: 0 10px 30px rgba(0,0,0,.45);
  }

  /* Front */
  .card--front { left: 50px; background: var(--card-dark); }
  .card--front .bands { position: absolute; inset: 0; }
  .front-wordmark {
    position: absolute; left: 44px; top: 58px;
    color: var(--brand-red); font-weight: 700;
    line-height: 1;
  }
  .front-wordmark .wm-name { display: block; font-size: 64px; letter-spacing: 2px; }
  .front-wordmark .wm-line { display: block; font-size: 15px; letter-spacing: .5px; margin-top: 8px; text-transform: uppercase; }

  /* Back */
  .card--back { left: 625px; background: var(--paper); }
  .card--back .panel {
    position: absolute; left: 0; top: 0; width: 200px; height: 100%;
    background: var(--panel-dark);
  }
  .card--back .accent-strip {
    position: absolute; left: 200px; top: 0; width: 45px; height: 100%;
    background: linear-gradient(to top, var(--brand-red) 0%, var(--brand-red) 40%, rgba(224,22,31,.15) 70%, rgba(224,22,31,0) 85%);
  }
  .name-tag {
    position: absolute; left: 150px; top: 118px;
    width: 150px; height: 54px;
    background: var(--paper);
    padding: 7px 0 0 18px;
    color: var(--brand-red);
    box-shadow: 0 2px 6px rgba(0,0,0,.18);
  }
  .name-tag .person-name { font-size: 17px; font-weight: 700; line-height: 1.1; }
  .name-tag .person-role { font-size: 12px; padding-left: 38px; }

  .back-wordmark {
    position: absolute; left: 300px; top: 70px;
    color: var(--ink); font-weight: 700; line-height: 1;
  }
  .back-wordmark .wm-name { display: block; font-size: 44px; letter-spacing: 2px; }
  .back-wordmark .wm-line { display: block; font-size: 10.5px; margin-top: 5px; text-transform: uppercase; }

  .contact-list {
    position: absolute; left: 258px; top: 198px;
    list-style: none; font-size: 12px; color: var(--ink);
  }
  .contact-list li { display: flex; align-items: center; gap: 7px; height: 17px; }
  .contact-list svg { width: 11px; height: 11px; flex: none; }
</style>
</head>
<body>
<main class="stage">

  <section class="card card--front" aria-label="Business card front">
    <svg class="bands" viewBox="0 0 525 300" width="525" height="300" aria-hidden="true">
      <defs>
        <linearGradient id="bandRed" x1="0" x2="1">
          <stop offset="0" stop-color="var(--deep-red)"/>
          <stop offset="1" stop-color="var(--brand-red)"/>
        </linearGradient>
      </defs>
      <polygon points="262,0 525,0 525,16 278,16" fill="url(#bandRed)"/>
      <polygon points="0,284 240,284 256,300 0,300" fill="url(#bandRed)"/>
    </svg>
    <div class="front-wordmark">
      <span class="wm-name">KORU</span>
      <span class="wm-line">Real Estate Holdings LLC</span>
    </div>
  </section>

  <section class="card card--back" aria-label="Business card back">
    <div class="panel"></div>
    <div class="accent-strip"></div>

    <div class="name-tag">
      <p class="person-name">YOUR NAME</p>
      <p class="person-role">Director</p>
    </div>

    <div class="back-wordmark">
      <span class="wm-name">KORU</span>
      <span class="wm-line">Real Estate Holdings LLC</span>
    </div>

    <ul class="contact-list">
      <li>
        <svg viewBox="0 0 12 12" aria-hidden="true"><rect width="12" height="12" rx="2" fill="var(--brand-red)"/><path d="M3.5 2.5h1.5l.8 2-1 .8a5 5 0 0 0 2 2l.8-1 2 .8V8.8a1 1 0 0 1-1 1A6.5 6.5 0 0 1 2.5 3.5a1 1 0 0 1 1-1z" fill="#fff"/></svg>
        0123 456 789
      </li>
      <li>
        <svg viewBox="0 0 12 12" aria-hidden="true"><rect width="12" height="12" rx="2" fill="var(--brand-red)"/><rect x="3" y="2.5" width="6" height="7" fill="#fff"/><rect x="4" y="3.5" width="4" height="2" fill="var(--brand-red)"/></svg>
        0123 456 789
      </li>
      <li>
        <svg viewBox="0 0 12 12" aria-hidden="true"><rect width="12" height="12" rx="2" fill="var(--brand-red)"/><rect x="2.5" y="3.5" width="7" height="5" fill="#fff"/><path d="M2.5 3.5 6 6.5 9.5 3.5" fill="none" stroke="var(--brand-red)" stroke-width=".9"/></svg>
        yourmail@koruholdings.com
      </li>
      <li>
        <svg viewBox="0 0 12 12" aria-hidden="true"><rect width="12" height="12" rx="2" fill="var(--brand-red)"/><path d="M6 10S3 6.8 3 5a3 3 0 0 1 6 0c0 1.8-3 5-3 5z" fill="#fff"/><circle cx="6" cy="5" r="1" fill="var(--brand-red)"/></svg>
        1100 Unknow Street, Anywhere, AnyCity.
      </li>
    </ul>
  </section>

</main>
</body>
</html>
```